Can you design a business card design? Looking for something unique and different. Can you design a business card design? Looking for something unique and different.Can you design a business card design? Looking for something unique and different.Can you design a business card design? Looking for something unique and different.Can you design a business card design? Looking for something unique and different.Can you design a business card design? Looking for something unique and different.

Industry/Entity Type

Business

Contact Information for Business Card

Can you design a business card design? Looking for something unique and different.

Font styles to use
Serif

```html
<!DOCTYPE html>
<html lang="en">
<head>
<meta charset="utf-8">
<title>Dosewell Business Card</title>
<link rel="stylesheet" href="https://fonts.googleapis.com/css2?family=Quicksand:wght@700&family=Montserrat:wght@400;500;600&display=swap">
<style>
  :root {
    --backdrop: #161616;
    --card-paper: #f3f3f2;
    --card-slate: #5b5b5b;
    --brand-purple: #9456d6;
    --ink-grey: #4a4a4a;
    --rule-grey: #8a8a8a;
    --white: #ffffff;
  }
  html, body {
    margin: 0;
    padding: 0;
    width: 1200px;
    height: 1000px;
    overflow: hidden;
    background: var(--backdrop);
  }
  .canvas {
    position: relative;
    width: 1200px;
    height: 1000px;
    background: var(--backdrop);
  }
  .hex-card {
    position: absolute;
  }
  /* Front side */
  .card-front {
    left: 250px;
    top: 242px;
    width: 385px;
    height: 323px;
    clip-path: polygon(0 50%, 24.7% 0, 75.3% 0, 100% 50%, 75.3% 100%, 24.7% 100%);
    background: var(--card-paper);
    font-family: "Montserrat", sans-serif;
    color: var(--ink-grey);
  }
  .brand-square {
    position: absolute;
    left: 172px;
    top: 22px;
    width: 40px;
    height: 40px;
    background: var(--brand-purple);
  }
  .brand-name {
    position: absolute;
    left: 0;
    right: 0;
    top: 108px;
    text-align: center;
    font-family: "Quicksand", sans-serif;
    font-weight: 700;
    font-size: 34px;
    line-height: 40px;
    color: var(--brand-purple);
  }
  .brand-descriptor {
    position: absolute;
    left: 90px;
    right: 90px;
    top: 149px;
    display: flex;
    align-items: center;
    gap: 6px;
    font-size: 8px;
    letter-spacing: 1.6px;
    color: var(--ink-grey);
    white-space: nowrap;
  }
  .brand-descriptor::before,
  .brand-descriptor::after {
    content: "";
    flex: 1;
    height: 1px;
    background: var(--rule-grey);
  }
  .name-band {
    position: absolute;
    left: 0;
    right: 0;
    top: 176px;
    height: 59px;
    background: var(--brand-purple);
    color: var(--white);
    text-align: center;
  }
  .person-name {
    margin: 10px 0 0;
    font-weight: 600;
    font-size: 17px;
    letter-spacing: 0.3px;
    line-height: 22px;
  }
  .person-title {
    margin: 0;
    font-size: 14px;
    line-height: 18px;
  }
  .contact-list {
    position: absolute;
    left: 0;
    right: 0;
    top: 246px;
    margin: 0;
    padding: 0;
    list-style: none;
    text-align: center;
    font-size: 13px;
    line-height: 21.5px;
    white-space: nowrap;
  }
  .contact-label {
    color: var(--brand-purple);
    font-weight: 600;
  }
  /* Back side */
  .card-back {
    left: 567px;
    top: 430px;
    width: 383px;
    height: 323px;
    clip-path: polygon(0 50%, 29.5% 0, 70.8% 0, 100% 50%, 70.8% 100%, 29.5% 100%);
    background: var(--card-slate);
    display: flex;
    flex-direction: column;
    align-items: center;
    justify-content: center;
    gap: 22px;
  }
  .back-square {
    width: 70px;
    height: 70px;
    background: var(--brand-purple);
  }
  .back-name {
    font-family: "Quicksand", sans-serif;
    font-weight: 700;
    font-size: 52px;
    line-height: 56px;
    color: var(--brand-purple);
  }
</style>
</head>
<body>
<main class="canvas">
  <section class="hex-card card-front" aria-label="Business card front">
    <div class="brand-square"></div>
    <div class="brand-name">Dosewell</div>
    <div class="brand-descriptor">cost management</div>
    <div class="name-band">
      <p class="person-name">MARLOW HAYES</p>
      <p class="person-title">President</p>
    </div>
    <ul class="contact-list">
      <li><span class="contact-label">E:</span> marlow.hayes@dosewell.com</li>
      <li><span class="contact-label">T:</span> 555-014-2716</li>
      <li><span class="contact-label">F:</span> 555-014-8830</li>
    </ul>
  </section>

  <section class="hex-card card-back" aria-label="Business card back">
    <div class="back-square"></div>
    <div class="back-name">Dosewell</div>
  </section>
</main>
</body>
</html>
```